Personal Finance Author needs a postcard

Hi there,

I am a Canadian personal finance author and have published a new book called The Coin Keeper.

I teach Millennials how to create a 6-figure portfolio through investing (https://www.miradabbot.example/)

I'm speaking at some conferences so we were going to print some postcards to hand out to attendees with our info and calls-to-action on them.

I am looking for 4x6 (horizontal) postcard (no space needed for shipping label).

Logos, Headshots and Book Cover:
https://files.example.net/share/9ZqLp72WxTbVn4KcRd0sHj3aE5uYgMfo?view=open

Both sides will be full colour. I would like a clean and simple look. Our main sites are www.MiraDabbot.example and www.TheCoinKeeperBook.example if you want to get a sense of style and design.
I also uploaded a few marketing materials so you can see the existing designs.

Side 1:
Get Instant Access to your Free Resources - main headline

(small bullets underneath)
- The Coin Keeper Checklist
- Financial Worksheets
- Database of Investment Tools

MiraDabbot.example/Resources

At the bottom, include "Don't forget to follow Mira Dabbot on social media:
Linkedin: @miradabbot7
Facebook: @thecoinkeeperbook Instagram: @thecoinkeeperbook Twitter: @CoinKeeperBook"

Side 2:
Headline - Want to work directly with Mira and The Coin Keeper team to help you make your money grow and stay safe?

Work with us to (bullet point list)...
- Hire Mira as a Keynote Speaker
- Teach Financial Literacy Workshops
- Receive Financial Coaching

Want To Learn More About How We Can Help?
MiraDabbot.example/Services

Include my contact info:
Mira Dabbot
Author | Speaker | Investor
mira@thecoinkeeperbook.example
555-274-0381

Target Market(s)

Millennials who want to learn how to save and invest their money. I focus on stock market investing, real estate investing and entrepreneurship.

Industry/Entity Type

Financial Service

Font styles to use
Sans Serif

Colors

Designer to choose colors to be used in the design.

Requirements
Must have
• Photo of Mira Dabbot
• The Coin Keeper logo
• Green, Gold/Yellow to match existing colours
• modern business style postcard

```html
<!DOCTYPE html>
<html lang="en">
<head>
<meta charset="utf-8">
<title>The Coin Keeper – Postcard</title>
<link href="https://fonts.googleapis.com/css2?family=Saira+Condensed:wght@600;700&family=Roboto+Condensed:ital,wght@0,400;0,700;1,700&display=swap" rel="stylesheet">
<style>
  :root {
    --green: #0f5e2c;
    --green-dark: #0b4a22;
    --gold: #d9a42b;
    --black: #1a1a1a;
    --ink: #222222;
    --paper: #ffffff;
    --card-border: #b9b9b9;
    --label: #555555;
    --photo-tone: #2b2b2f;
    --skin: #d9b79c;
  }
  * { box-sizing: border-box; margin: 0; padding: 0; }
  html, body { width: 1200px; height: 442px; overflow: hidden; background: var(--paper); }
  body { position: relative; font-family: "Roboto Condensed", "Arial Narrow", sans-serif; color: var(--ink); }

  .side-label {
    position: absolute; top: 6px;
    font-family: "Roboto Condensed", sans-serif; font-size: 19px; color: var(--label);
  }
  .card {
    position: absolute; top: 36px; width: 588px; height: 399px;
    border: 1px solid var(--card-border); overflow: hidden; background: var(--paper);
  }
  .card--front { left: 7px; }
  .card--back { left: 604px; }

  .backdrop {
    position: absolute; inset: 0;
    background: radial-gradient(ellipse at 50% 45%, #ffffff 20%, #eef1ea 70%, #e4e8df 100%);
  }

  .headline {
    position: absolute; font-family: "Saira Condensed", sans-serif; font-weight: 700;
    color: var(--green); text-transform: uppercase; line-height: 1.02;
  }

  .photo {
    position: absolute;
    background: linear-gradient(180deg, var(--skin) 0%, var(--skin) 16%, var(--photo-tone) 28%, var(--photo-tone) 100%);
    border-radius: 40% 40% 6px 6px / 14% 14% 6px 6px;
    opacity: .9;
  }

  /* Front */
  .brand-name {
    position: absolute; left: 30px; top: 56px; width: 120px; text-align: center;
    font-family: "Saira Condensed", sans-serif; font-weight: 700; font-size: 27px;
    line-height: 1.05; color: var(--green);
  }

  .book-cover {
    position: absolute; left: 30px; top: 136px; width: 132px; height: 228px;
    background: linear-gradient(160deg, #f7f5ef 0%, #e8e2cf 55%, var(--green) 56%, var(--green-dark) 100%);
    border-radius: 3px; box-shadow: 3px 4px 8px rgba(0,0,0,.25);
  }
  .card--front .headline { left: 205px; top: 40px; font-size: 31px; }

  .resource-list { position: absolute; left: 206px; top: 125px; list-style: none; }
  .resource-list li {
    display: flex; align-items: center; gap: 7px; height: 23.5px;
    font-size: 15.5px; color: var(--ink);
  }
  .tick { width: 10px; height: 10px; flex: none; }

  .web-link {
    position: absolute; display: flex; align-items: center; gap: 5px;
    font-weight: 700; font-style: italic; color: var(--green);
  }
  .card--front .web-link { left: 205px; top: 218px; font-size: 16px; }
  .globe { width: 14px; height: 14px; flex: none; }

  .social-accent { position: absolute; left: 330px; top: 246px; width: 110px; height: 7px; background: var(--green); }
  .social-box {
    position: absolute; left: 194px; top: 252px; width: 246px; height: 76px;
    background: var(--gold); border-radius: 38px 0 0 38px; padding: 7px 0 0 26px;
  }
  .social-box__title {
    font-family: "Saira Condensed", sans-serif; font-weight: 700; font-size: 13.5px;
    line-height: 1.05; color: var(--black);
  }
  .social-handles {
    list-style: none; display: grid; grid-template-columns: 120px 110px; row-gap: 3px;
    margin: 7px 0 0 -14px; font-size: 10px; color: var(--black);
  }
  .social-handles li { display: flex; align-items: center; gap: 4px; }
  .social-handles li::before { content: ""; width: 8px; height: 8px; background: var(--black); border-radius: 1px; }

  .card--front .photo { left: 462px; top: 76px; width: 104px; height: 300px; }

  .footer-rule { position: absolute; left: 0; right: 0; top: 375px; height: 3px; background: var(--gold); }
  .footer-band { position: absolute; right: 0; top: 371px; width: 300px; height: 13px; background: var(--black); clip-path: polygon(4% 0, 100% 0, 100% 100%, 0 100%); }
  .card--back .footer-band { width: 260px; }

  /* Back */
  .card--back .headline { left: 22px; top: 40px; font-size: 26px; }
  .section-title {
    position: absolute; font-family: "Saira Condensed", sans-serif; font-weight: 700;
    text-transform: uppercase; line-height: 1;
  }
  .section-title--work { left: 22px; top: 144px; font-size: 21px; color: var(--green); }
  .service-list { position: absolute; left: 24px; top: 174px; list-style: none; }
  .service-list li {
    display: flex; align-items: center; gap: 4px; height: 21px; font-size: 16.5px; color: var(--ink);
  }
  .service-list .tick { width: 9px; height: 9px; }

  .section-title--contact { left: 22px; top: 256px; font-size: 28px; color: var(--gold); }
  .contact-details { position: absolute; left: 26px; top: 286px; font-size: 12.5px; line-height: 16px; color: var(--ink); font-style: normal; }
  .contact-name { font-weight: 700; font-style: italic; }
  .phone {
    position: absolute; left: 24px; top: 347px; display: flex; align-items: center; gap: 6px;
    font-family: "Saira Condensed", sans-serif; font-weight: 700; font-size: 24px; color: var(--green);
  }
  .phone svg { width: 19px; height: 19px; }

  .card--back .photo { left: 420px; top: 120px; width: 150px; height: 180px; }

  .cta-pill {
    position: absolute; left: 284px; top: 281px; width: 304px; height: 64px;
    background: var(--green); border-radius: 32px 0 0 32px;
    display: flex; align-items: center; justify-content: flex-end; padding-right: 28px;
    font-family: "Saira Condensed", sans-serif; font-weight: 700; font-size: 21px; line-height: 1;
    color: #ffffff; text-align: right; text-transform: uppercase;
  }
  .card--back .web-link { right: 30px; top: 350px; font-size: 15px; }
</style>
</head>
<body>
  <div class="side-label" style="left:8px">FRONT</div>
  <div class="side-label" style="left:604px">BACK</div>

  <section class="card card--front">
    <div class="backdrop" role="img" aria-label="Faint pattern of banknotes across the background"></div>

    <div class="brand-name">The Coin Keeper</div>
    <div class="book-cover" role="img" aria-label="Stack of The Coin Keeper books by Mira Dabbot"></div>

    <h1 class="headline">Get instant access to your<br>free resources</h1>
    <ul class="resource-list">
      <li><svg class="tick" viewBox="0 0 10 10"><path d="M1 5.5 L4 8.5 L9 1.5" fill="none" stroke="#d9a42b" stroke-width="2"/></svg>The Coin Keeper Checklist</li>
      <li><svg class="tick" viewBox="0 0 10 10"><path d="M1 5.5 L4 8.5 L9 1.5" fill="none" stroke="#d9a42b" stroke-width="2"/></svg>Financial Worksheets</li>
      <li><svg class="tick" viewBox="0 0 10 10"><path d="M1 5.5 L4 8.5 L9 1.5" fill="none" stroke="#d9a42b" stroke-width="2"/></svg>Database of Investment Tools</li>
    </ul>
    <div class="web-link">
      <svg class="globe" viewBox="0 0 14 14" fill="none" stroke="#0f5e2c" stroke-width="1.3"><circle cx="7" cy="7" r="6"/><ellipse cx="7" cy="7" rx="2.6" ry="6"/><path d="M1 7h12M2 4h10M2 10h10"/></svg>
      MiraDabbot.example/Resources
    </div>

    <div class="social-accent"></div>
    <div class="social-box">
      <p class="social-box__title">Don't forget to follow<br>Mira Dabbot on social media:</p>
      <ul class="social-handles">
        <li>@miradabbot7</li>
        <li>@thecoinkeeperbook</li>
        <li>@thecoinkeeperbook</li>
        <li>@CoinKeeperBook</li>
      </ul>
    </div>

    <div class="photo" role="img" aria-label="Photo of Mira Dabbot in a dark suit, seated on a black chair"></div>

    <div class="footer-rule"></div>
    <div class="footer-band"></div>
  </section>

  <section class="card card--back">
    <div class="backdrop" role="img" aria-label="Faint pattern of banknotes across the background"></div>

    <h2 class="headline">Want to work directly with Mira and<br>The Coin Keeper team to help you make<br>your money grow and stay safe?</h2>

    <h3 class="section-title section-title--work">Work with us to</h3>
    <ul class="service-list">
      <li><svg class="tick" viewBox="0 0 10 10"><path d="M1 5.5 L4 8.5 L9 1.5" fill="none" stroke="#222" stroke-width="1.8"/></svg>Hire Mira as a Keynote Speaker</li>
      <li><svg class="tick" viewBox="0 0 10 10"><path d="M1 5.5 L4 8.5 L9 1.5" fill="none" stroke="#222" stroke-width="1.8"/></svg>Teach Financial Literacy Workshops</li>
      <li><svg class="tick" viewBox="0 0 10 10"><path d="M1 5.5 L4 8.5 L9 1.5" fill="none" stroke="#222" stroke-width="1.8"/></svg>Receive Financial Coaching</li>
    </ul>

    <h3 class="section-title section-title--contact">Contact</h3>
    <address class="contact-details">
      <div class="contact-name">Mira Dabbot</div>
      <div>Author | Speaker | Investor</div>
      <div>mira@thecoinkeeperbook.example</div>
    </address>
    <div class="phone">
      <svg viewBox="0 0 20 20"><rect width="20" height="20" rx="4" fill="#0f5e2c"/><path d="M6 4.5c-1 .6-1.6 1.6-1.2 3 .9 3.4 3.9 6.6 7.6 7.7 1.3.4 2.3-.2 2.9-1.1l-2.3-2-1.4 1c-1.6-.7-3-2.2-3.8-3.9l1-1.4z" fill="#fff"/></svg>
      555-274-0381
    </div>

    <div class="photo" role="img" aria-label="Photo of Mira Dabbot smiling, holding a calculator and pointing at it"></div>

    <div class="cta-pill">Want to learn more<br>about how we can help?</div>
    <div class="web-link">
      <svg class="globe" viewBox="0 0 14 14" fill="none" stroke="#0f5e2c" stroke-width="1.3"><circle cx="7" cy="7" r="6"/><ellipse cx="7" cy="7" rx="2.6" ry="6"/><path d="M1 7h12M2 4h10M2 10h10"/></svg>
      MiraDabbot.example/Services
    </div>

    <div class="footer-rule"></div>
    <div class="footer-band"></div>
  </section>
</body>
</html>
```